Business Card Design Project for a Restaurant/Wine Bar

New, fresh business card design for Verdano Wine Bar & Restaurant, Tidecrest, Corvale. We are an established restaurant on the Corvale coast featuring "Italian coastal cuisine."

"Verdano" means bay leaf in Italian. We aren't sure if we would like our logo on the card or not, but if you have something interesting that uses it, then please do so. The basic information is essential - full restaurant name, address, phone and website (do not use www). The font on our menu and wine list may give you some sort of an idea of our style.

One-sided card needed as we often use the backside to write down various types of info for customers.

After seeing a few submissions, we would like to see what designers can come up with-using the logo, just the leaf, or none at all. Sky is the limit as long as our full restaurant name, address, phone and website (please leave out www) are there. Please contact us if questions!

I appreciate all of your designs! Our deadline is next week, but I will continue to give feedback on designs as I can. This is our busiest season, so my co-owner/chef/husband, won't have time to look at the designs for awhile. When he does, we can make our decision.

cheers,
Mirel

Target Market(s)

Fine dining/wine crowd. Would like something simple and elegant, but not pretentious or stuffy. Verdano means bay laurel (bay leaf) in Italian (please see our logo).

Industry/Entity Type

Restaurant

Requirements
Must have
• Full Name of Restaurant: Verdano Wine Bar & Restaurant
Address: 812 Fenwick Ave NW, Tidecrest, Corvale 97538
Phone: 541.555.0193
website: verdanowinebar.example (do not use www)
Should not have
• Loud colors.

```html
<!DOCTYPE html>
<html lang="en">
<head>
<meta charset="utf-8">
<title>Verdano Wine Bar &amp; Restaurant — Business Card</title>
<link rel="stylesheet" href="https://fonts.googleapis.com/css2?family=Libre+Baskerville:wght@400;700&display=swap">
<style>
  :root {
    --page-bg: #e9e6e1;
    --card-black: #0b0b0c;
    --card-sheen: #2a2b2d;
    --leaf-green: #8cc63f;
    --name-white: #f4f4f2;
    --muted-grey: #c9c9c6;
    --body-white: #e6e6e3;
  }
  * { box-sizing: border-box; margin: 0; padding: 0; }
  html, body {
    width: 1200px;
    height: 900px;
    overflow: hidden;
    background: var(--page-bg);
  }
  .canvas {
    width: 1200px;
    height: 900px;
    display: flex;
    align-items: center;
    justify-content: center;
  }
  .business-card {
    position: relative;
    width: 700px;
    height: 400px;
    background: var(--card-black);
    overflow: hidden;
    box-shadow: 0 18px 40px rgba(0,0,0,0.28);
    font-family: "Libre Baskerville", Georgia, serif;
  }
  .card-art {
    position: absolute;
    inset: 0;
    width: 100%;
    height: 100%;
  }
  .brand-block {
    position: absolute;
    right: 56px;
    top: 44px;
    text-align: right;
    line-height: 1;
  }
  .brand-name {
    font-size: 66px;
    font-weight: 400;
    color: var(--name-white);
    letter-spacing: 1px;
  }
  .brand-sub {
    margin-top: 6px;
    font-size: 40px;
    color: var(--muted-grey);
  }
  .brand-tag {
    margin-top: 8px;
    font-size: 17px;
    letter-spacing: 2.5px;
    color: var(--leaf-green);
    text-transform: uppercase;
  }
  .contact-block {
    position: absolute;
    left: 60px;
    bottom: 48px;
    line-height: 1.45;
    font-style: normal;
  }
  .contact-address {
    font-size: 15px;
    color: var(--body-white);
  }
  .contact-phone {
    margin-top: 10px;
    font-size: 22px;
    color: var(--leaf-green);
  }
  .contact-web {
    font-size: 15px;
    color: var(--leaf-green);
  }
</style>
</head>
<body>
<main class="canvas">
  <article class="business-card">
    <svg class="card-art" viewBox="0 0 700 400" aria-hidden="true">
      <defs>
        <radialGradient id="top-sheen" cx="62%" cy="30%" r="55%">
          <stop offset="0" stop-color="#2a2b2d"/>
          <stop offset="1" stop-color="#0b0b0c"/>
        </radialGradient>
        <linearGradient id="lower-fade" x1="0" y1="0" x2="1" y2="1">
          <stop offset="0" stop-color="#141516"/>
          <stop offset="1" stop-color="#070707"/>
        </linearGradient>
      </defs>
      <rect class="upper-panel" width="700" height="400" fill="url(#top-sheen)"/>
      <path class="lower-panel" d="M0 170 C 220 190, 470 215, 700 236 L700 400 L0 400 Z" fill="url(#lower-fade)"/>
      <path class="green-swoosh" d="M0 160 C 220 178, 470 205, 700 236 C 470 214, 220 192, 0 176 Z" fill="#8cc63f"/>
    </svg>

    <header class="brand-block">
      <div class="brand-name">Verdano</div>
      <div class="brand-sub">Wine Bar</div>
      <div class="brand-tag">&amp; Restaurant</div>
    </header>

    <address class="contact-block">
      <div class="contact-address">812 Fenwick Ave NW, Tidecrest<br>Corvale 97538</div>
      <div class="contact-phone">541.555.0193</div>
      <div class="contact-web">verdanowinebar.example</div>
    </address>
  </article>
</main>
</body>
</html>
```